Lantern Holdings Business Card

We are looking to design new business cards for our company. We have two office locations and would like to have both full addresses on the card. Each address needs two lines for the building name and street address and a line or two for the city, state and zip code. There should be a place for 2-3 phone numbers. The addresses and phone numbers are at the bottom of this description. We also need a place to put our company website and one email address. Our logo is attached.
We would like the card to be two sided. The back of the card should have a blue background with some part of our logo design on it. We would like the full logo on the front of the card as well. The front of the card should have a white background with the blue logo. We are open to listing our addresses on the front or the back of the card. The person who designed our logo gave us an excellent business card idea that we really liked. I have attached a picture of his business card idea so that we can build off of it.
Addresses:
The Marlow Exchange
2214 47th Street NW
Washington, DC 20419
Osprey Harbor Tower
815 Tamsin Boulevard #2207
Miami, FL 33987
Phone Numbers: (202) 555-0148
(202) 555-0193
Website: www.lanternholdings-example.com

```html
<!DOCTYPE html>
<html lang="en">
<head>
<meta charset="utf-8">
<title>Lantern Holdings Business Card</title>
<link rel="stylesheet" href="https://fonts.googleapis.com/css2?family=Arimo:wght@400&family=Cinzel:wght@500&display=swap">
<style>
  :root {
    --navy: #1b1a66;
    --ink: #2a2a8c;
    --paper: #ffffff;
    --edge: #b9b9c8;
    --page: #ffffff;
  }
  * { box-sizing: border-box; margin: 0; padding: 0; }
  html, body { width: 776px; height: 1200px; overflow: hidden; background: var(--page); }
  .sheet { position: relative; width: 776px; height: 1200px; }

  .card {
    position: absolute;
    width: 300px;
    height: 510px;
    border-radius: 16px;
    overflow: hidden;
  }
  .card--navy { background: var(--navy); color: var(--paper); }
  .card--white { background: var(--paper); color: var(--ink); border: 1.5px solid var(--edge); }

  .card--back-a  { left: 44px;  top: 40px; }
  .card--back-b  { left: 427px; top: 40px; }
  .card--front-a { left: 44px;  top: 645px; }
  .card--front-b { left: 427px; top: 645px; }

  .band { position: absolute; inset: 0; width: 100%; height: 100%; }

  .wordmark {
    position: absolute;
    display: flex;
    align-items: center;
    font-family: "Cinzel", serif;
    font-weight: 500;
    font-size: 23px;
    line-height: 1.1;
    letter-spacing: 0.5px;
  }
  .wordmark__mark { width: 28px; height: 28px; flex: none; }

  .wordmark--flipped {
    left: 14px; top: 196px; width: 274px; height: 70px;
    transform: rotate(180deg);
    color: var(--paper);
  }
  .wordmark--flipped .wordmark__mark { background: var(--paper); }
  .wordmark--flipped .wordmark__name { margin-left: auto; width: 180px; }

  .wordmark--upright {
    left: 62px; top: 222px;
    color: var(--navy);
  }
  .wordmark--upright .wordmark__mark { background: var(--paper); }
  .wordmark--upright .wordmark__name { margin-left: 22px; }

  .front-mark {
    position: absolute;
    left: 210px; top: 40px;
    width: 54px; height: 54px;
  }
  .card--white .front-mark { background: var(--navy); }
  .card--navy .front-mark { background: var(--paper); }

  .contact {
    position: absolute;
    left: 16px; top: 240px;
    width: 272px;
    font-family: "Arimo", sans-serif;
    font-size: 14px;
    line-height: 18px;
  }
  .contact__home { width: 20px; height: 20px; display: block; margin-bottom: 4px; }
  .office { margin-bottom: 12px; }
  .phones { display: flex; align-items: flex-start; gap: 6px; margin-top: 4px; }
  .phones__icon { width: 14px; height: 30px; flex: none; margin-top: 4px; }
  .phones__list { padding-left: 4px; }
  .online { margin-top: 12px; padding-left: 24px; }
</style>
</head>
<body>
<main class="sheet">

  <section class="card card--navy card--back-a" aria-label="Card back, navy">
    <svg class="band" viewBox="0 0 300 510" preserveAspectRatio="none" aria-hidden="true">
      <polygon points="168,0 214,0 298,510 250,510" fill="var(--paper)"/>
    </svg>
    <div class="wordmark wordmark--flipped">
      <span class="wordmark__mark"></span>
      <span class="wordmark__name">LANTERN<br>HOLDINGS</span>
    </div>
  </section>

  <section class="card card--white card--back-b" aria-label="Card back, white">
    <svg class="band" viewBox="0 0 300 510" preserveAspectRatio="none" aria-hidden="true">
      <polygon points="0,0 55,0 158,510 104,510" fill="var(--navy)"/>
    </svg>
    <div class="wordmark wordmark--upright">
      <span class="wordmark__mark"></span>
      <span class="wordmark__name">LANTERN<br>HOLDINGS</span>
    </div>
  </section>

  <section class="card card--white card--front-a" aria-label="Card front, white">
    <span class="front-mark"></span>
    <div class="contact">
      <svg class="contact__home" viewBox="0 0 20 20" aria-hidden="true">
        <polygon points="10,1 19,10 16,10 16,19 4,19 4,10 1,10" fill="currentColor"/>
      </svg>
      <p class="office">The Marlow Exchange<br>2214 47th Street NW<br>Washington, DC 20419</p>
      <p class="office">Osprey Harbor Tower<br>815 Tamsin Boulevard #2207<br>Miami, FL 33987</p>
      <div class="phones">
        <svg class="phones__icon" viewBox="0 0 14 30" aria-hidden="true">
          <path d="M4,1 C1,2 0,6 0,15 C0,24 1,28 4,29 L7,28 L6,20 L3,20 C2,17 2,13 3,10 L6,10 L7,2 Z" fill="currentColor"/>
        </svg>
        <p class="phones__list">Phone Numbers: (202) 555-0148<br>(202) 555-0193</p>
      </div>
      <p class="online">www.lanternholdings-example.com<br>info@lanternholdings-example.com</p>
    </div>
  </section>

  <section class="card card--navy card--front-b" aria-label="Card front, navy">
    <span class="front-mark"></span>
    <div class="contact">
      <svg class="contact__home" viewBox="0 0 20 20" aria-hidden="true">
        <polygon points="10,1 19,10 16,10 16,19 4,19 4,10 1,10" fill="currentColor"/>
      </svg>
      <p class="office">The Marlow Exchange<br>2214 47th Street NW<br>Washington, DC 20419</p>
      <p class="office">Osprey Harbor Tower<br>815 Tamsin Boulevard #2207<br>Miami, FL 33987</p>
      <div class="phones">
        <svg class="phones__icon" viewBox="0 0 14 30" aria-hidden="true">
          <path d="M4,1 C1,2 0,6 0,15 C0,24 1,28 4,29 L7,28 L6,20 L3,20 C2,17 2,13 3,10 L6,10 L7,2 Z" fill="currentColor"/>
        </svg>
        <p class="phones__list">Phone Numbers: (202) 555-0148<br>(202) 555-0193</p>
      </div>
      <p class="online">www.lanternholdings-example.com<br>info@lanternholdings-example.com</p>
    </div>
  </section>

</main>
</body>
</html>
```